Flyer for an online formula one racing league

Hello.

I am looking for the perfect one page facebook/instagram style flyer for an online formula one racing league. The racing league is called 'VOLKA RACING LEAGUE'.

Information that MUST be on the new flyer is already on the old flyer I have uploaded here. In addition to including: The Volka racing league 'R' logo I have uploaded AND the text: 'Very popular, clean and competitive racing league, running for its 4th season. Why not join with a friend? Race times, Mondays, Tuesdays and Wednesdays each at 8pm UK TIME Message below for any questions. (Spacing of information is not important, however all the information in regards to the racing I have just mentioned MUST BE on the flyer, this includes info from old pic, logo and the other info I just mentioned).

It would be beneficial to have lots of dark blue on the flyer and the new flyer to be a lot different to the original flyer I uploaded, but this is not essential.

I apologise if I did not explain very well, any questions, please message me.

The best flyer should look the most attractive to someone that might be interested in joining an online formula one racing league.

I used this website before to create the perfect logo for my Sunday League team last year, and I was very impressed. I look forward to seeing your submissions.

Target Market(s)

No specific target, more something that may attract someone into joining a formula one online racing league

Industry/Entity Type

e sports/formula one

Colors
0054AA
0677BA
7BADD7
CADEEF
E8F1F8

Requirements
Must have
• Read product description please
Should not have
• Ignoring product description!

```html
<!DOCTYPE html>
<html lang="en">
<head>
<meta charset="utf-8">
<title>Volka Racing League – Flyer</title>
<link rel="stylesheet" href="https://fonts.googleapis.com/css2?family=Bebas+Neue&family=Poppins:wght@400;500;700;800&display=swap">
<style>
  :root {
    --navy: #0f1f6e;
    --panel-light: #22389c;
    --panel-dark: #132480;
    --blue: #1212e6;
    --pink: #e8088a;
    --yellow: #ffd200;
    --white: #ffffff;
    --ink: #1d1d1f;
    --ink-navy: #16226a;
  }
  * { margin: 0; padding: 0; box-sizing: border-box; }
  html, body { width: 1200px; height: 710px; overflow: hidden; background: #ffffff; }
  .flyer {
    position: relative; width: 1200px; height: 710px; overflow: hidden;
    background: var(--navy);
    font-family: "Poppins", Arial, sans-serif;
  }
  .band { position: absolute; left: 0; width: 1200px; }
  .band--header { top: 45px; height: 212px; background: var(--white); }
  .band--feature {
    top: 257px; height: 273px;
    background: radial-gradient(ellipse at 50% 45%, var(--panel-light) 0%, var(--panel-dark) 70%);
  }
  .band--schedule { top: 530px; height: 161px; background: var(--white); }

  .brand-mark {
    position: absolute; left: 41px; top: 44px; width: 210px; height: 210px;
    border-radius: 50%; background: #0b1035;
    display: flex; align-items: center; justify-content: center;
    color: var(--white); font-weight: 800; font-size: 40px; letter-spacing: 1px;
  }

  .title {
    position: absolute; left: 292px; top: 62px;
    font-family: "Bebas Neue", Impact, sans-serif; font-size: 134px; line-height: 1;
    white-space: nowrap; transform: scaleY(1.12); transform-origin: left top;
  }
  .title__name { color: var(--blue); }
  .title__league { color: var(--pink); }
  .tagline {
    position: absolute; left: 292px; top: 204px;
    font-weight: 700; font-size: 25px; color: var(--ink); white-space: nowrap;
  }

  .headline {
    position: absolute; top: 278px;
    font-weight: 800; font-size: 62px; line-height: 64px; white-space: nowrap;
  }
  .headline--season { left: 53px; color: var(--pink); }
  .headline--friend { left: 648px; color: var(--white); }
  .divider-v { position: absolute; border-left: 2px dotted rgba(255,255,255,0.75); }
  .divider-v--feature { left: 604px; top: 284px; height: 140px; }
  .divider-h {
    position: absolute; left: 25px; top: 438px; width: 1143px;
    border-top: 2px dotted rgba(255,255,255,0.75);
  }
  .growth {
    position: absolute; left: 0; top: 446px; width: 1200px; text-align: center;
    font-family: "Bebas Neue", Impact, sans-serif; font-size: 62px; line-height: 1;
    color: var(--yellow); white-space: nowrap;
    transform: scaleY(1.22); transform-origin: center top;
  }

  .race-times {
    position: absolute; left: 56px; top: 557px;
    font-weight: 700; font-size: 44px; line-height: 46px; color: var(--pink);
  }
  .race-days {
    position: absolute; left: 212px; top: 560px;
    font-weight: 700; font-size: 26px; color: var(--blue); white-space: nowrap;
  }
  .race-slot { position: absolute; left: 212px; top: 610px; display: flex; align-items: center; }
  .race-slot__label {
    font-weight: 700; font-size: 19px; line-height: 21px; color: var(--pink);
  }
  .race-slot__time {
    margin: 0 14px 0 16px; padding: 4px 10px 2px; border-radius: 10px;
    background: var(--yellow); color: var(--navy);
    font-family: "Bebas Neue", Impact, sans-serif; font-size: 34px; line-height: 1;
  }
  .race-slot__note {
    margin-left: 36px; font-weight: 500; font-size: 21px; line-height: 22px;
    color: var(--ink); letter-spacing: 0.5px;
  }
  .divider-v--schedule { left: 794px; top: 553px; height: 112px; border-left-color: var(--ink-navy); }
  .spaces { position: absolute; left: 848px; top: 565px; }
  .spaces__label {
    font-weight: 500; font-size: 24px; letter-spacing: 4.5px; color: var(--ink-navy);
  }
  .spaces__days {
    margin-top: 4px; font-weight: 700; font-size: 25px; line-height: 30px; color: var(--pink);
  }
</style>
</head>
<body>
  <main class="flyer">
    <div class="band band--header"></div>
    <div class="band band--feature"></div>
    <div class="band band--schedule"></div>

    <div class="brand-mark">VOLKA</div>

    <h1 class="title"><span class="title__name">VOLKA RACING</span> <span class="title__league">LEAGUE</span></h1>
    <p class="tagline">VERY POPULAR, CLEAN AND COMPETITIVE RACING LEAGUE</p>

    <p class="headline headline--season">RUNNING FOR<br>ITS 4TH SEASON</p>
    <span class="divider-v divider-v--feature"></span>
    <p class="headline headline--friend">WHY NOT JOIN<br>WITH A FRIEND?</p>
    <span class="divider-h"></span>
    <p class="growth">3 DIVISIONS CURRENTLY AND LOOKING TO KEEP GROWING!</p>

    <p class="race-times">RACE<br>TIMES</p>
    <p class="race-days">MONDAYS, TUESDAYS &amp;WEDNESDAYS</p>
    <div class="race-slot">
      <span class="race-slot__label">EACH<br>AT</span>
      <span class="race-slot__time">8PM</span>
      <span class="race-slot__label">UK<br>TIME</span>
      <span class="race-slot__note">MASSAGE BELOW FOR ANY<br>QUESTIONS</span>
    </div>
    <span class="divider-v divider-v--schedule"></span>
    <div class="spaces">
      <p class="spaces__label">SPACES LEFT ON</p>
      <p class="spaces__days">MONDAYS,TUESDAY<br>&amp; WEDNESDAYS!!!</p>
    </div>
  </main>
</body>
</html>
```